website design for Company KMV

Our company name KMV(the civic canvas limited), need design a website. It is a website that focuses on promoting art design in the world.
We will provide the existing logo design, the new website and logo should be matched to each other. The website has to include pages "Home" "Contact" "Service" and So on at least 6-8 pages. The site is mainly for publicity and promotion. We will have an existing domain and hosting.
Updates

We prefer the original design, thanks.

Target Market(s)

large public art

Industry/Entity Type

Architecture and design, large public art and sculpture manufacturer

Coding

Coded - Design and coding required

Number of Pages Required

5+ page

Requirements
Must have
• 1. the overall color has to match our logo color 2. Do not need to do any change on our logo including the color 3. Here is a similar style of the home page we like, it can be similar but must not same. Pls check the below link. https://www.darveno.example/en-us/

```html
<!DOCTYPE html>
<html lang="en">
<head>
<meta charset="utf-8">
<title>KMV – The Civic Canvas Limited</title>
<link href="https://fonts.googleapis.com/css2?family=Teko:wght@400;500;600&family=Rubik:wght@400;500&display=swap" rel="stylesheet">
<style>
:root{
  --orange:#f05a28;
  --orange-dark:#c8431a;
  --ink:#2a2a2a;
  --dark:#1c1c1e;
  --charcoal:#2f2f31;
  --grey-text:#9b9b9b;
  --body-text:#4a4a4a;
  --white:#ffffff;
  --heading:'Teko',sans-serif;
  --text:'Rubik',sans-serif;
}
*{margin:0;padding:0;box-sizing:border-box}
html,body{width:1200px;height:4060px;overflow:hidden;background:var(--white)}
body{position:relative;font-family:var(--text);color:var(--body-text)}
.abs{position:absolute}
.btn{position:absolute;display:flex;align-items:center;justify-content:center;background:var(--orange);color:var(--white);font-family:var(--heading);font-size:17px;letter-spacing:.5px;text-transform:uppercase;clip-path:polygon(0 0,96% 0,100% 100%,0 100%);box-shadow:inset -4px -3px 0 var(--orange-dark)}
.brand{font-family:var(--text);font-weight:500;letter-spacing:1px;text-transform:uppercase;display:flex;align-items:center;gap:10px}
.brand .mark{width:14px;height:14px;background:var(--orange)}
.heading{font-family:var(--heading);font-weight:500;text-transform:uppercase;line-height:.9}

/* hero */
.hero{top:0;left:0;width:1200px;height:690px;clip-path:polygon(0 0,100% 0,100% 630px,0 690px);background:radial-gradient(ellipse at 50% 45%,#7a1512 0%,#3a0d0c 28%,#1a1a1c 60%,#0e0e10 100%)}
.topbar{top:0;left:158px;width:882px;height:55px;display:flex;align-items:center;justify-content:space-between;color:#ddd;font-size:13px}
.topbar b{color:var(--white);font-weight:500}
.topbar .ico{display:inline-block;width:14px;height:12px;vertical-align:middle;margin-right:10px}
.social{display:flex;gap:6px;margin-left:20px}
.social span{width:26px;height:26px;border:1px solid #666;display:block}
.nav{top:60px;left:158px;width:882px;height:46px;display:flex;align-items:center}
.nav .brand{color:var(--white);font-size:18px}
.nav ul{list-style:none;display:flex;gap:38px;margin-left:auto;margin-right:40px;font-family:var(--heading);font-size:20px;color:var(--white)}
.nav .btn{position:relative;width:118px;height:34px;font-size:17px}
.hero h1{top:258px;left:0;width:1200px;text-align:center;color:var(--white);font-size:72px;line-height:66px}
.hero p{top:394px;left:0;width:1200px;text-align:center;color:var(--white);font-size:14px;line-height:22px}
.arrow-box{width:63px;height:42px;display:flex;align-items:center;justify-content:center}

/* about */
.about-art{top:690px;left:0;width:480px;height:360px;background:linear-gradient(90deg,#e8e8e8,#f4f4f4 70%,#fff)}
.about .brand{color:var(--ink);font-size:22px}
.about h2{color:var(--grey-text);font-size:52px;line-height:52px}
.about p{font-size:13.5px;line-height:23.6px;color:var(--body-text)}

/* services */
.services{top:1000px;left:0;width:1200px;height:955px;clip-path:polygon(0 50px,100% 0,100% 900px,0 955px);background:radial-gradient(circle at 50% 55%,#3a3a3a 0%,#262627 40%,#1a1a1b 100%)}
.section-title{color:var(--white);text-align:center;font-size:56px}
.section-sub{color:#e8e8e8;text-align:center;font-size:14px;line-height:23px}
.hex{position:absolute;width:283px;height:325px;clip-path:polygon(50% 0,100% 15%,100% 80%,50% 100%,0 80%,0 15%);background:var(--white);text-align:center}
.hex .photo{height:168px}
.hex h3{font-family:var(--text);font-weight:500;font-size:18px;color:var(--ink);margin-top:20px}
.hex p{font-size:14px;line-height:23px;color:#555;margin:6px 28px 0}
.hex .go{width:36px;height:26px;margin:10px auto 0;background:#e4e4e4;display:flex;align-items:center;justify-content:center}
.hex.featured{background:var(--orange)}
.hex.featured h3,.hex.featured p{color:var(--white)}
.hex.featured .go{background:#f27a50}

/* why */
.why h2{color:var(--ink);font-size:54px}
.why p{font-size:13.5px;line-height:23.6px;color:var(--body-text)}

/* gallery */
.gallery{top:2380px;left:0;width:1200px;height:805px;clip-path:polygon(0 56px,100% 0,100% 750px,0 805px);background:radial-gradient(ellipse at 70% 10%,#3c3c3e 0%,#2d2d2f 45%,#2a2a2b 100%)}
.tile{position:absolute}

/* artists */
.artist-box{top:3256px;left:158px;width:282px;height:360px;background:#2b2b2c;color:var(--white);padding:44px 26px}
.artist-box h2{font-size:52px;line-height:48px}
.artist-box p{font-size:13.5px;line-height:23.6px;color:#e0e0e0;margin-top:12px}
.artist{position:absolute;width:200px;text-align:center}
.artist .face{width:142px;height:142px;border-radius:50%;margin:0 auto;border:4px solid var(--orange)}
.artist h3{font-family:var(--text);font-weight:500;font-size:18px;color:var(--ink);margin-top:18px}
.artist span{display:block;font-size:13.5px;color:#666;margin-top:3px}
.artist .go{width:36px;height:26px;margin:18px auto 0;background:#e4e4e4;display:flex;align-items:center;justify-content:center}

/* footer */
.footer{top:3660px;left:0;width:1200px;height:400px;clip-path:polygon(0 58px,100% 0,100% 100%,0 100%);background:linear-gradient(180deg,#2a2a2c 0%,#1e1e20 60%,#19191a 100%)}
.footer h4{font-family:var(--heading);font-weight:500;font-size:26px;color:var(--white);text-align:center;text-transform:uppercase}
.contact{position:absolute;display:flex;align-items:center;gap:16px;color:#ccc;font-size:13px;line-height:20px}
.contact b{color:var(--white);font-weight:400;display:block}
.contact .ring{width:50px;height:50px;border-radius:50%;border:1px solid #aaa;display:flex;align-items:center;justify-content:center}
.bottombar{top:3982px;left:0;width:1200px;height:78px;background:#141415}
</style>
</head>
<body>

<!-- hero -->
<section class="hero abs" role="img" aria-label="Night photograph of a large red arched steel sculpture among city towers">
</section>
<div class="topbar abs">
  <div><svg class="ico" viewBox="0 0 14 12"><path d="M0 4 7 0l7 4v8H0z" fill="#f05a28"/><path d="M0 4l7 4 7-4" stroke="#fff" fill="none"/></svg>Mail Us: <b>info@kmv.example</b></div>
  <div style="display:flex;align-items:center"><svg class="ico" viewBox="0 0 14 14"><path d="M3 1l3 3-2 2c1 2 2 3 4 4l2-2 3 3-2 2C6 13 1 8 1 3z" fill="#f05a28"/></svg>Call Us: <b>&nbsp;123-456-7890</b>
    <div class="social"><span aria-label="social link"></span><span aria-label="social link"></span><span aria-label="social link"></span></div></div>
</div>
<nav class="nav abs">
  <div class="brand"><span class="mark"></span>KMV The Civic Canvas</div>
  <ul><li>Home</li><li>Service ▾</li><li>Contact</li></ul>
  <div class="btn">Get Started</div>
</nav>
<h1 class="heading abs hero-title" style="top:258px;left:0;width:1200px;text-align:center;color:#fff;font-size:72px;line-height:66px">Promoting Art<br>Design in the World.</h1>
<p class="abs" style="top:394px;left:0;width:1200px;text-align:center;color:#fff;font-size:14px;line-height:22px">Lorem ipsum dolor sit amet consectetur adipiscing elit sed<br>do eiusmod tempor incididunt ut labore et dolore</p>
<div class="btn" style="top:458px;left:538px;width:124px;height:36px">Learn More</div>
<div class="arrow-box abs" style="top:323px;left:150px;background:rgba(120,120,120,.55)"><svg width="42" height="14" viewBox="0 0 42 14"><path d="M42 7H2M8 1 2 7l6 6" stroke="#fff" stroke-width="2" fill="none"/></svg></div>
<div class="arrow-box abs" style="top:323px;left:985px;background:var(--orange)"><svg width="42" height="14" viewBox="0 0 42 14"><path d="M0 7h40M34 1l6 6-6 6" stroke="#fff" stroke-width="2" fill="none"/></svg></div>

<!-- about -->
<section class="about">
  <div class="about-art abs" role="img" aria-label="Faded pencil sketch of a figure"></div>
  <div class="brand abs" style="top:748px;left:158px;color:var(--ink);font-size:22px"><span class="mark"></span>KMV The Civic Canvas</div>
  <h2 class="heading abs" style="top:800px;left:158px;width:340px">About the Civic Canvas Limited</h2>
  <div class="btn" style="top:924px;left:162px;width:120px;height:36px">Learn More</div>
  <div class="abs" style="top:738px;left:544px;width:2px;height:192px;background:var(--orange)"></div>
  <p class="abs" style="top:762px;left:571px;width:470px">Lorem ipsum dolor sit amet, consectetur adipisicing elit, sed do enim eiusmod tempor incididunt ut labore et dolore magna aliqua. Ut enim ad minim veniam, quis nostrud exercitation ullamco laboris nisi ut sed aliquip ex ea commodo consequat. Duis aute irure dolor in repreheder in voluptate velit esse cillum dolore eu fugiat nulla pariatur. Excepteur sint occaecat cupidatat non proident, sunt in culpa qui official.</p>
</section>

<!-- services -->
<section class="services abs" role="img" aria-label="Dark photograph of a spiral staircase seen from above"></section>
<h2 class="heading section-title abs" style="top:1088px;left:0;width:1200px">Our Services</h2>
<p class="section-sub abs" style="top:1147px;left:0;width:1200px">Lorem ipsum dolor sit amet consectetur adipiscing elit sed do eiusmod<br>tempor incididunt ut labore et dolore magna aliqua.</p>

<div class="hex" style="top:1254px;left:158px"><div class="photo" role="img" aria-label="Curved copper architectural canopy" style="background:linear-gradient(160deg,#c9c5c2,#d9772a 55%,#3a2414)"></div><h3>Architecture &amp; Design</h3><p>Lorem ipsum dolor sit amet nulla adipisicing elit sed do..</p><div class="go"><svg width="20" height="20" viewBox="0 0 20 20"><circle cx="10" cy="10" r="8" fill="none" stroke="#f05a28" stroke-width="1.5"/><path d="M6 10h8M11 7l3 3-3 3" stroke="#f05a28" stroke-width="1.5" fill="none"/></svg></div></div>
<div class="hex featured" style="top:1254px;left:458px"><div class="photo" role="img" aria-label="Street mural painted on a wall" style="background:linear-gradient(150deg,#c23a4e,#7a3a5a 50%,#3c3440)"></div><h3>Large Public Art</h3><p>Lorem ipsum dolor sit amet nulla adipisicing elit sed do..</p><div class="go"><svg width="20" height="20" viewBox="0 0 20 20"><circle cx="10" cy="10" r="8" fill="none" stroke="#fff" stroke-width="1.5"/><path d="M6 10h8M11 7l3 3-3 3" stroke="#fff" stroke-width="1.5" fill="none"/></svg></div></div>
<div class="abs" style="top:1262px;left:632px;width:76px;height:76px;border-radius:50%;background:#fff;border:3px solid #f2d5c8;display:flex;align-items:center;justify-content:center"><svg width="40" height="36" viewBox="0 0 40 36"><rect x="3" y="3" width="34" height="24" fill="none" stroke="#f05a28" stroke-width="2"/><path d="M10 33h20M20 27v6M9 10h22M9 16h14" stroke="#f05a28" stroke-width="2"/></svg></div>
<div class="hex" style="top:1254px;left:758px"><div class="photo" role="img" aria-label="Carved relief sculpture on a stone facade" style="background:linear-gradient(160deg,#a8785a,#d6a27a 50%,#8a5c44)"></div><h3>Sculpture Manufacture</h3><p>Lorem ipsum dolor sit amet nulla adipisicing elit sed do..</p><div class="go"><svg width="20" height="20" viewBox="0 0 20 20"><circle cx="10" cy="10" r="8" fill="none" stroke="#f05a28" stroke-width="1.5"/><path d="M6 10h8M11 7l3 3-3 3" stroke="#f05a28" stroke-width="1.5" fill="none"/></svg></div></div>
<div class="hex" style="top:1514px;left:308px"><div class="photo" role="img" aria-label="City skyline at night through a viewing window" style="background:linear-gradient(160deg,#2a3050,#5a5468 50%,#b08a50)"></div><h3>Lorem Ipsum Amet</h3><p>Lorem ipsum dolor sit amet nulla adipisicing elit sed do..</p><div class="go"><svg width="20" height="20" viewBox="0 0 20 20"><circle cx="10" cy="10" r="8" fill="none" stroke="#f05a28" stroke-width="1.5"/><path d="M6 10h8M11 7l3 3-3 3" stroke="#f05a28" stroke-width="1.5" fill="none"/></svg></div></div>
<div class="hex" style="top:1514px;left:608px"><div class="photo" role="img" aria-label="Bronze equestrian statue against the sky" style="background:linear-gradient(170deg,#dfe6ee,#9aa4b4 50%,#3a3e48)"></div><h3>Lorem Ipsum Amet</h3><p>Lorem ipsum dolor sit amet nulla adipisicing elit sed do..</p><div class="go"><svg width="20" height="20" viewBox="0 0 20 20"><circle cx="10" cy="10" r="8" fill="none" stroke="#f05a28" stroke-width="1.5"/><path d="M6 10h8M11 7l3 3-3 3" stroke="#f05a28" stroke-width="1.5" fill="none"/></svg></div></div>

<!-- why -->
<section class="why">
  <h2 class="heading abs" style="top:2022px;left:158px">Why Chose Us</h2>
  <p class="abs" style="top:2076px;left:158px;width:440px">Perspiciatis unde omnis iste natus error sit voluptatem accusantium doloremque laudantium, totam rem aperiam, eaque ipsa quae velit illo inventore veritatis et quasi architecto beatae vitae dicta suntiler explicabo. Nemo enim ipsam voluptatem quia voluptas sit nisi utba aliquip ex ea commodo consequat uis aute irure dolor.</p>
  <p class="abs" style="top:2208px;left:158px;width:440px">Magni dolores eos qui ratione voluptatem sequi nesciunt. Neque sed porro quisquam est, qui dolorem ipsum quia dolor sit amet dolore in consectetur, adipisci velit, sed quia non numquam eius.</p>
  <div class="btn" style="top:2304px;left:162px;width:120px;height:36px">Learn More</div>
  <svg class="abs" style="top:1987px;left:646px" width="394" height="334" viewBox="0 0 394 334" role="img" aria-label="Colourful street art collage framed in a large letter-shaped triangle">
    <defs><linearGradient id="collage" x1="0" y1="0" x2="1" y2="1"><stop offset="0" stop-color="#9fc4e8"/><stop offset=".35" stop-color="#c7453a"/><stop offset=".6" stop-color="#e0a22a"/><stop offset=".8" stop-color="#6a3fa0"/><stop offset="1" stop-color="#2e6ab0"/></linearGradient></defs>
    <path d="M166 0h60l168 334H0z M196 78 106 266h180z" fill="url(#collage)" fill-rule="evenodd"/>
  </svg>
</section>

<!-- gallery -->
<section class="gallery abs" role="img" aria-label="Dark background with soft grey curved forms"></section>
<h2 class="heading section-title abs" style="top:2468px;left:0;width:1200px">Our Art Gallery</h2>
<p class="section-sub abs" style="top:2526px;left:0;width:1200px">Duis aute irure dolor in reprehenderit in voluptate velit esse cillum<br>dolore eu fugiat nulla pariatur. Excepteur sint occaecat cupi.</p>
<div class="tile" role="img" aria-label="Abstract carved wooden sculptures on a tiled floor" style="top:2605px;left:158px;width:283px;height:404px;background:linear-gradient(170deg,#8a6a5a,#5a3a2e 50%,#8aa0b0)"></div>
<div class="tile" role="img" aria-label="Gallery hall with paintings and a bronze seated figure" style="top:2605px;left:458px;width:282px;height:191px;background:linear-gradient(160deg,#8a2a22,#5a2a22 60%,#2a2222);display:flex;align-items:center;justify-content:center"><svg width="40" height="40" viewBox="0 0 40 40"><circle cx="17" cy="17" r="12" fill="none" stroke="#fff" stroke-width="1.5"/><path d="M26 26l10 10M17 12v10M12 17h10" stroke="#fff" stroke-width="1.5"/></svg></div>
<div class="tile" role="img" aria-label="Painted red door among flower planters" style="top:2605px;left:758px;width:283px;height:191px;background:linear-gradient(160deg,#d8c8b8,#c0402e 55%,#5a7a3a)"></div>
<div class="tile" role="img" aria-label="Spiral skylight ceiling seen from below" style="top:2818px;left:458px;width:282px;height:191px;background:radial-gradient(circle,#4a8ae0 0%,#2a6a8a 30%,#7a4a3a 65%,#3a2a2a 100%)"></div>
<div class="tile" role="img" aria-label="Modern curved glass building by the sea" style="top:2818px;left:758px;width:283px;height:191px;background:linear-gradient(180deg,#e8ecef,#b8c2ca 40%,#5a5248 80%,#8a8a80)"></div>
<div class="btn" style="top:3046px;left:538px;width:124px;height:36px">Load More</div>

<!-- artists -->
<div class="artist-box abs">
  <h2 class="heading">View Our<br>Artist</h2>
  <p>Perspiciatis unde omnis iste natus error sit voluptatem accusantium doloremque laudantium, totam rem aperiam, eaque ipsa quae velit illo inventore veritatis et quasi.</p>
  <div class="btn" style="top:294px;left:28px;width:120px;height:36px">View More</div>
</div>
<svg class="abs" style="top:3303px;left:440px" width="16" height="24" viewBox="0 0 16 24"><path d="M0 0l16 12L0 24z" fill="#2b2b2c"/></svg>
<div class="artist" style="top:3330px;left:485px"><div class="face" role="img" aria-label="Portrait of an architecture designer" style="background:linear-gradient(160deg,#5a7a4a,#c8a890)"></div><h3>Ethan Marlow</h3><span>Architecture Designer</span><div class="go"><svg width="20" height="20" viewBox="0 0 20 20"><circle cx="10" cy="10" r="8" fill="none" stroke="#f05a28" stroke-width="1.5"/><path d="M6 10h8M11 7l3 3-3 3" stroke="#f05a28" stroke-width="1.5" fill="none"/></svg></div></div>
<div class="artist" style="top:3330px;left:677px"><div class="face" role="img" aria-label="Portrait of an artist" style="background:linear-gradient(160deg,#3a3432,#a8887a)"></div><h3>Rafael Ostrin</h3><span>Artist</span><div class="go"><svg width="20" height="20" viewBox="0 0 20 20"><circle cx="10" cy="10" r="8" fill="none" stroke="#f05a28" stroke-width="1.5"/><path d="M6 10h8M11 7l3 3-3 3" stroke="#f05a28" stroke-width="1.5" fill="none"/></svg></div></div>
<div class="artist" style="top:3330px;left:868px"><div class="face" role="img" aria-label="Portrait of a sculpture designer" style="background:linear-gradient(160deg,#e8e8ea,#d8a890)"></div><h3>Colby Danner</h3><span>Sculpture Design</span><div class="go"><svg width="20" height="20" viewBox="0 0 20 20"><circle cx="10" cy="10" r="8" fill="none" stroke="#f05a28" stroke-width="1.5"/><path d="M6 10h8M11 7l3 3-3 3" stroke="#f05a28" stroke-width="1.5" fill="none"/></svg></div></div>

<!-- footer -->
<section class="footer abs" role="img" aria-label="Dark photograph of a statue silhouetted against palm trees"></section>
<h4 class="abs" style="top:3746px;left:0;width:1200px">Sign Up for Newsletter</h4>
<div class="abs" style="top:3796px;left:380px;width:306px;height:36px;background:#fff;font-size:13px;color:#555;padding:10px 18px">Enter your email.</div>
<div class="btn" style="top:3796px;left:695px;width:122px;height:36px">Subscribe</div>
<div class="contact" style="top:3870px;left:213px"><div class="ring"><svg width="20" height="20" viewBox="0 0 14 14"><path d="M3 1l3 3-2 2c1 2 2 3 4 4l2-2 3 3-2 2C6 13 1 8 1 3z" fill="#f05a28"/></svg></div><div>Call Us:<b>123-456-7890</b></div></div>
<div class="abs" style="top:3872px;left:414px;width:1px;height:44px;background:#555"></div>
<div class="contact" style="top:3870px;left:465px"><div class="ring"><svg width="20" height="18" viewBox="0 0 14 12"><path d="M0 4 7 0l7 4v8H0z" fill="#f05a28"/><path d="M0 4l7 4 7-4" stroke="#fff" fill="none"/></svg></div><div>Mail Us:<b>info@kmv.example</b></div></div>
<div class="abs" style="top:3872px;left:668px;width:1px;height:44px;background:#555"></div>
<div class="contact" style="top:3870px;left:719px"><div class="ring"><svg width="16" height="22" viewBox="0 0 16 22"><path d="M8 0a8 8 0 0 1 8 8c0 6-8 14-8 14S0 14 0 8a8 8 0 0 1 8-8z" fill="#f05a28"/><circle cx="8" cy="8" r="3" fill="#fff"/></svg></div><div>Location:<b>Sed ut perspiciatis unde omnis</b></div></div>
<div class="bottombar abs"></div>
<div class="social abs" style="top:4006px;left:158px;margin:0;gap:12px"><span aria-label="social link" style="width:30px;height:30px;border-color:#777"></span><span aria-label="social link" style="width:30px;height:30px;border-color:#777"></span><span aria-label="social link" style="width:30px;height:30px;border-color:#777"></span></div>
<div class="brand abs" style="top:4010px;left:0;width:1200px;justify-content:center;color:#fff;font-size:18px"><span class="mark"></span>KMV The Civic Canvas</div>
<p class="abs" style="top:4000px;left:830px;width:210px;text-align:right;font-size:13px;line-height:21px;color:#bbb">Copyright © 2021 The Civic Canvas.<br>All rights reserved.</p>

</body>
</html>
```